Korellas Einfühlungsvermögen in das Projekt, ihre Nachfragen an der richtigen Stelle und ihre frischen Ideen haben zu einem ebook-Cover geführt, mit dem ich sehr zufrieden bin. Die Kommunikation war sehr angenehm und professionell. Danke!
Zielgruppe
E-Book: Satirische Kurzgeschichten rund um Schule und Bildung.
Zielgruppe: Leute mit Humor und Interesse an einem Einblick ins Klassenzimmer einer jungen Berliner Lehrerin. Schüler, Eltern, Lehrer, Referendare...
Aufgabenstellung
Möglichst keine Comics mit Sprechblasen, eher stilvoll, intellektuell, trotzdem frisch, jung und modern.
Helle Farben, gerne Andeutungen der Themen Schule, Bildung, Unterricht.
Die Kurzgeschichten meines E-Books sind schnelle Momentaufnahmen, sie könnten auch als Blog erscheinen statt als Buch, evtl. lässt sich dies auch im Design widerspiegeln (?).

```html
<!DOCTYPE html>
<html lang="de">
<head>
<meta charset="utf-8">
<title>Kreide und Kaffee – Helga Prinz</title>
<link rel="stylesheet" href="https://fonts.googleapis.com/css2?family=EB+Garamond:wght@500&family=Dancing+Script:wght@600&family=Itim&display=swap">
<style>
  :root {
    --sky: #80d6f0;
    --sky-deep: #6fcdea;
    --dress: #c42a3a;
    --dress-deep: #b3232f;
    --label: #ffffff;
    --author-red: #c8213f;
    --title-yellow: #f7f24a;
    --subtitle-cyan: #35c1ec;
  }
  html, body {
    margin: 0;
    padding: 0;
    width: 800px;
    height: 1200px;
    overflow: hidden;
    background: var(--sky);
  }
  .cover {
    position: relative;
    width: 800px;
    height: 1200px;
    overflow: hidden;
  }
  .cover-photo {
    position: absolute;
    inset: 0;
    background: linear-gradient(180deg,
      var(--sky) 0%,
      var(--sky-deep) 34%,
      var(--dress) 62%,
      var(--dress-deep) 100%);
  }
  .author-label {
    position: absolute;
    left: 209px;
    top: 161px;
    width: 449px;
    height: 178px;
    background: var(--label);
    display: flex;
    align-items: center;
    justify-content: center;
  }
  .author-name {
    margin: 0;
    font-family: "EB Garamond", Georgia, serif;
    font-weight: 500;
    font-size: 52px;
    letter-spacing: -0.5px;
    text-transform: uppercase;
    color: var(--author-red);
    line-height: 1;
  }
  .book-title {
    position: absolute;
    left: 0;
    width: 800px;
    top: 420px;
    margin: 0;
    text-align: center;
    font-family: "Dancing Script", cursive;
    font-weight: 600;
    font-size: 112px;
    line-height: 230px;
    color: var(--title-yellow);
  }
  .book-title span { display: block; height: 210px; line-height: 190px; }
  .book-subtitle {
    position: absolute;
    left: 0;
    width: 800px;
    top: 840px;
    margin: 0;
    text-align: center;
    font-family: "Itim", sans-serif;
    font-weight: 400;
    font-size: 78px;
    line-height: 106px;
    color: var(--subtitle-cyan);
  }
  .book-subtitle span { display: block; }
</style>
</head>
<body>
  <main class="cover">
    <div class="cover-photo" role="img" aria-label="Foto: junge Lehrerin im roten Punktekleid vor hellblauem Hintergrund, einen Bücherstapel auf der Hand balancierend"></div>

    <div class="author-label">
      <p class="author-name">Helga Prinz</p>
    </div>

    <h1 class="book-title">
      <span>Kreide und</span>
      <span>Kaffee.</span>
    </h1>

    <h2 class="book-subtitle">
      <span>Notizen</span>
      <span>vom</span>
      <span>Lehrerpult</span>
    </h2>
  </main>
</body>
</html>
```